Email Marketing Campaign Templates

Email drip childcare campaign designed to communicate with parents interested in services. We would like the template(s) to be created so that we can change the content as needed.I will add below collateral that we have used in the past as well as logo.
three to for templates 1.) welcome template 2/ things to bring 3) generic template
Target Market(s)
Parents and Millennials
Industry/Entity Type
Childcare
Colors
85cae6
0493ce
9bcb3c
add136
fefefe
faa54b
cadf82
86cae7
33a6d7
Requirements
Must have
- Photos of staff with children
Nice to have
- Photos

```html
<!DOCTYPE html>
<html lang="en">
<head>
<meta charset="utf-8">
<title>Meadow Early Learning Center – Welcome</title>
<link rel="stylesheet" href="https://fonts.googleapis.com/css2?family=Courgette&family=Tinos&display=swap">
<style>
  :root {
    --orange: #f4a21c;
    --blue: #1b8bd6;
    --blue-deep: #1279c2;
    --green: #9bcb3c;
    --green-light: #cadf82;
    --white: #fefefe;
    --footer: #3b3b3b;
    --ink-soft: #eaf5fb;
  }
  * { margin: 0; padding: 0; box-sizing: border-box; }
  html, body { width: 1200px; height: 3016px; overflow: hidden; background: var(--white); }
  .email { position: relative; width: 1200px; height: 3016px; overflow: hidden; font-family: "Tinos", "Times New Roman", serif; }

  .hero-photo {
    position: absolute; left: 0; top: 0; width: 1200px; height: 1120px;
    background: linear-gradient(160deg, #b89a74 0%, #8c6c4c 35%, #5d6f7a 65%, #c2a47c 100%);
  }

  .brand {
    position: absolute; left: 0; top: 0; width: 560px; height: 420px;
    background: var(--white); border-radius: 0 0 280px 0;
    display: flex; flex-direction: column; align-items: center; justify-content: center;
    padding: 0 70px 30px 20px; gap: 18px;
  }
  .brand-dot { width: 120px; height: 120px; border-radius: 50%; background: var(--green); }
  .brand-name { font-family: "Courgette", cursive; color: var(--blue-deep); font-size: 58px; line-height: 1.05; text-align: center; }

  .welcome {
    position: absolute; left: 0; top: 1060px; width: 1200px; height: 1460px;
    background: var(--orange);
  }
  .waves { position: absolute; left: 0; width: 1200px; }
  .wave-top { top: 1020px; height: 120px; }
  .wave-bottom { top: 2420px; height: 160px; }

  .welcome-title {
    position: absolute; left: 40px; top: 1190px; width: 1120px;
    font-family: "Courgette", cursive; color: var(--white);
    font-size: 62px; line-height: 1.2; text-align: center;
  }
  .welcome-body {
    position: absolute; left: 70px; top: 1378px; width: 1060px;
    color: var(--white); font-size: 34px; line-height: 1.22; text-align: center;
  }

  .gallery-photo {
    position: absolute; width: 520px; height: 340px;
    border: 8px solid var(--white);
  }
  .p1 { left: 60px; top: 1680px; background: linear-gradient(135deg, #7d8aa0, #c49a6a 60%, #6b8f5a); }
  .p2 { left: 620px; top: 1680px; background: linear-gradient(135deg, #d8c6b4, #a4785c 50%, #e8e2dc); }
  .p3 { left: 60px; top: 2060px; background: linear-gradient(135deg, #c98a70, #e6d2c0 50%, #7a6a64); }
  .p4 { left: 620px; top: 2060px; background: linear-gradient(135deg, #d4c8b8, #6c7d9a 50%, #c94a3c); }

  .contact {
    position: absolute; left: 0; top: 2520px; width: 1200px; height: 420px;
    background: var(--blue);
  }
  .contact-text {
    position: absolute; left: 0; top: 2588px; width: 1200px;
    color: var(--white); font-size: 36px; line-height: 1.3; text-align: center;
  }
  .contact-text p { margin-bottom: 22px; }
  .contact-text p.address { margin-bottom: 26px; }

  .footer {
    position: absolute; left: 0; top: 2940px; width: 1200px; height: 76px;
    background: var(--footer); color: var(--white);
    font-size: 34px; display: flex; align-items: center; justify-content: center;
  }
</style>
</head>
<body>
<div class="email">
  <div class="hero-photo" role="img" aria-label="Photo of young children working at a classroom table with a teacher"></div>

  <div class="brand">
    <div class="brand-dot"></div>
    <div class="brand-name">Meadow Early Learning Center</div>
  </div>

  <div class="welcome"></div>
  <svg class="waves wave-top" viewBox="0 0 1200 120" preserveAspectRatio="none" aria-hidden="true">
    <path d="M0 70 C300 20 700 20 1200 30 L1200 120 L0 120 Z" fill="var(--green)"/>
    <path d="M0 84 C300 36 700 36 1200 46 L1200 120 L0 120 Z" fill="var(--white)"/>
    <path d="M0 96 C300 52 700 52 1200 60 L1200 120 L0 120 Z" fill="var(--orange)"/>
  </svg>

  <h1 class="welcome-title">Welcome to our children&nbsp; at<br>meadow early learning center</h1>
  <p class="welcome-body">Lorem Ipsum is simply dummy text of the printing and typesetting industry. Lorem Ipsum has been the industry's standard dummy text ever since the 1500s, when an unknown printer took a galley of type and scrambled it to make a type specimen book.</p>

  <div class="gallery-photo p1" role="img" aria-label="Photo of children doing a table activity in class"></div>
  <div class="gallery-photo p2" role="img" aria-label="Photo of a teacher reading a tablet with a toddler"></div>
  <div class="gallery-photo p3" role="img" aria-label="Photo of toddlers playing at a craft table"></div>
  <div class="gallery-photo p4" role="img" aria-label="Photo of a child playing on a classroom rug"></div>

  <div class="contact"></div>
  <svg class="waves wave-bottom" viewBox="0 0 1200 160" preserveAspectRatio="none" aria-hidden="true">
    <path d="M0 60 C400 130 800 20 1200 70 L1200 160 L0 160 Z" fill="var(--white)"/>
    <path d="M0 76 C400 146 800 36 1200 86 L1200 160 L0 160 Z" fill="var(--blue)"/>
  </svg>

  <div class="contact-text">
    <p class="address">We are conveniently located in Downtown Maplewood:<br>208 West Orchard Avenue Maplewood, Ohio 43299</p>
    <p>Hours : &nbsp;Monday – Friday : &nbsp;7:00 a.m. – 6:00 p.m.</p>
    <p>Phone: 555-014-2290.</p>
    <p>We can't wait to meet your family!</p>
  </div>

  <div class="footer">Copyright@meadowearlylearning</div>
</div>
</body>
</html>
```